Business Cards and Logo

KWM - Personal Injury Attorneys is the name of the firm.
We are personal injury lawyers. We want a crisp, modern and impactful design.
Color schemes are white, matte black and light grey OR white, matte black and red OR white, matte black and a nice blue or yellow.
For logo - we don’t want typical logos like scales of justice or a hammer. We want a general design with the KWM letters.
Target Market(s)
People who need attorneys.
Industry/Entity Type
Law Firm
Contact Information for Business Card
Back side: text: Los Angeles - Santa Ana - San Diego - San Francisco
Front side
Name of firm and logo.
Marco Feltrovski
812 W. Colter Ave. 4th Floor
Glendale, CA 91207
(818)555-0172 (c)
(818)555-0194 (o)
Marco@fieldcounselwest.example
Logo Text
KWM
Font styles to use
Other font styles liked:
- Musk - regular. Military - regular. Moonglade. Future. Or similar fonts.
Requirements
Must have
- See above. Nothing else to provide.
- KWM - Personal Injury Attorneys is the name of the firm.
- We are personal injury lawyers. We want a crisp, modern and impactful design.
- Color schemes are white, matte black and light grey OR white, matte black and red OR white, matte black and a nice blue or yellow.
- For logo - we don’t want typical logos like scales of justice or a hammer. We want a general design with the KWM letters.
Nice to have
- See above - nothing else to provide.
Should not have

```html
<!DOCTYPE html>
<html lang="en">
<head>
<meta charset="utf-8">
<title>KWM - Personal Injury Attorneys - Business Cards</title>
<link href="https://fonts.googleapis.com/css2?family=Barlow+Semi+Condensed:wght@500;600;700&family=Barlow:wght@300;400;500&display=swap" rel="stylesheet">
<style>
  :root {
    --stage: #2b2e33;
    --ink: #121212;
    --paper: #ffffff;
    --brand-blue: #1f3fa3;
    --text-dark: #2a2a2a;
  }
  * { box-sizing: border-box; margin: 0; padding: 0; }
  html, body { width: 1200px; height: 900px; overflow: hidden; }
  body {
    background: var(--stage);
    font-family: "Barlow", sans-serif;
    position: relative;
  }
  .card {
    position: absolute;
    width: 520px;
    height: 297px;
    overflow: hidden;
    box-shadow: 0 18px 40px rgba(0,0,0,.45);
  }
  .card-back { left: 40px; top: 150px; background: var(--ink); color: var(--paper); }
  .card-front { left: 640px; top: 150px; background: var(--paper); }
  .card-shapes { position: absolute; inset: 0; }

  .lockup { display: flex; align-items: center; position: absolute; }
  .lockup-name {
    font-family: "Barlow Semi Condensed", sans-serif;
    font-weight: 700;
    letter-spacing: 1px;
    line-height: 1;
  }
  .lockup-rule { align-self: stretch; width: 2px; }
  .lockup-tagline {
    font-family: "Barlow Semi Condensed", sans-serif;
    font-weight: 600;
    line-height: 0.98;
    text-transform: uppercase;
  }

  /* back side */
  .card-back .lockup { left: 70px; top: 92px; }
  .card-back .lockup-name { font-size: 62px; color: var(--paper); }
  .card-back .lockup-rule { background: var(--paper); margin: 0 20px; }
  .card-back .lockup-tagline { font-size: 31px; color: var(--paper); }
  .office-cities {
    position: absolute; left: 70px; top: 200px;
    font-size: 15px; font-weight: 300; letter-spacing: .4px;
  }

  /* front side */
  .card-front .lockup { left: 28px; top: 22px; }
  .card-front .lockup-name { font-size: 36px; color: var(--brand-blue); }
  .card-front .lockup-rule { background: var(--ink); margin: 0 12px; }
  .card-front .lockup-tagline { font-size: 18px; color: var(--ink); }
  .office-address {
    position: absolute; left: 30px; top: 166px;
    font-size: 12.5px; line-height: 1.3; color: var(--text-dark);
    font-style: normal;
  }
  .contact-block {
    position: absolute; right: 26px; top: 164px;
    text-align: right; color: var(--paper);
  }
  .attorney-name {
    font-family: "Barlow Semi Condensed", sans-serif;
    font-weight: 700; font-size: 22px; margin-bottom: 8px;
  }
  .contact-line {
    display: flex; justify-content: flex-end; align-items: center;
    gap: 8px; font-size: 13.5px; line-height: 1.45;
  }
  .contact-line svg { width: 13px; height: 13px; flex: none; }

  /* presentation lockup */
  .brand-lockup { right: 70px; bottom: 70px; height: 66px; }
  .brand-lockup .lockup-name { font-size: 66px; color: var(--paper); }
  .brand-lockup .lockup-rule { background: var(--paper); margin: 0 20px; }
  .brand-lockup .lockup-tagline { font-size: 33px; color: var(--paper); }
</style>
</head>
<body>

  <section class="card card-back" aria-label="Business card back">
    <div class="lockup">
      <span class="lockup-name">KWM</span>
      <span class="lockup-rule"></span>
      <span class="lockup-tagline">Personal<br>Injury Attorneys</span>
    </div>
    <p class="office-cities">Los Angeles - Santa Ana - San Diego - San Francisco</p>
  </section>

  <section class="card card-front" aria-label="Business card front">
    <svg class="card-shapes" viewBox="0 0 520 297" aria-hidden="true">
      <rect x="0" y="86" width="520" height="34" fill="var(--brand-blue)"/>
      <polygon points="0,120 290,120 270,146 0,146" fill="var(--ink)"/>
      <polygon points="410,0 520,0 520,297 150,297" fill="var(--brand-blue)"/>
    </svg>

    <div class="lockup">
      <span class="lockup-name">KWM</span>
      <span class="lockup-rule"></span>
      <span class="lockup-tagline">Personal<br>Injury Attorneys</span>
    </div>

    <address class="office-address">
      812 W. Colter Ave.<br>4th Floor, Glendale<br>CA 91207
    </address>

    <div class="contact-block">
      <p class="attorney-name">Marco Feltrovski</p>
      <p class="contact-line">(818)555-0172
        <svg viewBox="0 0 12 12"><rect x="3" y="0.7" width="6" height="10.6" rx="1" fill="none" stroke="#fff" stroke-width="1.2"/><circle cx="6" cy="9.5" r=".6" fill="#fff"/></svg>
      </p>
      <p class="contact-line">(818)555-0194
        <svg viewBox="0 0 12 12"><path d="M1 4.5C1 2.5 3.5 1.8 6 1.8S11 2.5 11 4.5L9 5 8.3 3.8H3.7L3 5Z" fill="#fff"/><path d="M3.3 5.5h5.4L10 10.5H2Z" fill="#fff"/><circle cx="6" cy="8" r="1.2" fill="var(--brand-blue)"/></svg>
      </p>
      <p class="contact-line">Marco@fieldcounselwest.example
        <svg viewBox="0 0 12 12"><rect x="0.5" y="2.5" width="11" height="7.5" fill="#fff"/><path d="M0.8 2.8 6 7l5.2-4.2" fill="none" stroke="var(--brand-blue)" stroke-width="1"/></svg>
      </p>
      <p class="contact-line">www.fieldcounselwest.example
        <svg viewBox="0 0 12 12"><circle cx="6" cy="6" r="5.2" fill="none" stroke="#fff" stroke-width="1.1"/><ellipse cx="6" cy="6" rx="2.2" ry="5.2" fill="none" stroke="#fff" stroke-width="1"/><path d="M1 6h10M1.8 3.5h8.4M1.8 8.5h8.4" stroke="#fff" stroke-width="1"/></svg>
      </p>
    </div>
  </section>

  <div class="lockup brand-lockup" aria-label="KWM Personal Injury Attorneys">
    <span class="lockup-name">KWM</span>
    <span class="lockup-rule"></span>
    <span class="lockup-tagline">Personal<br>Injury Attorneys</span>
  </div>

</body>
</html>
```